7 Vex Label

Design a label for 7 Vex styling gels. The logo is attached. The color is C=100, M=100, Y=0, K=0. The 16 oz. jar is also attached.

Updates

Attention all designers,

The old logo has been deleted.  I have uploaded a new logo for this project.  Can you please update your design with the NEW LOGO?
thank you,
Rob

Target Market(s)

Multicultural

Requirements
Must have
• you must used the logo attached.

text to be included on the jar:

Used by Professionals
Maximum Hold
Alcohol Free
NO FLAKING

16 oz.

As far as label size, use the jar photo, and fit the design on it.

```html
<!DOCTYPE html>
<html lang="en">
<head>
<meta charset="utf-8">
<title>7 Vex Styling Gel Label</title>
<link href="https://fonts.googleapis.com/css2?family=Federo&family=Arimo:wght@400;700&display=swap" rel="stylesheet">
<style>
  :root {
    --stage: #ececec;
    --label: #ffffff;
    --label-edge: #8a8a8a;
    --brand-purple: #3a3189;
    --title-red: #e6254e;
    --bullet-red: #e8264f;
    --white: #ffffff;
  }
  html, body {
    margin: 0;
    padding: 0;
    width: 1200px;
    height: 1000px;
    overflow: hidden;
    background: var(--stage);
  }
  .canvas {
    position: relative;
    width: 1200px;
    height: 1000px;
  }
  .label {
    position: absolute;
    left: 100px;
    top: 150px;
    width: 1000px;
    height: 700px;
    background: var(--label);
    border: 2px solid var(--label-edge);
    box-sizing: border-box;
    overflow: hidden;
  }
  .product-title {
    position: absolute;
    left: 86px;
    top: 46px;
    margin: 0;
    font-family: "Federo", sans-serif;
    font-weight: 400;
    font-size: 150px;
    line-height: 1;
    color: var(--title-red);
    transform: scaleX(0.78);
    transform-origin: left top;
    letter-spacing: 2px;
    white-space: nowrap;
  }
  .claims {
    position: absolute;
    left: 0;
    top: 336px;
    margin: 0;
    padding: 0;
    list-style: none;
    font-family: "Arimo", Arial, sans-serif;
    font-size: 35px;
    line-height: 45px;
    color: var(--brand-purple);
  }
  .claims li {
    position: relative;
    padding-left: 34px;
  }
  .claims li::before {
    content: "";
    position: absolute;
    left: -8px;
    top: 13px;
    width: 18px;
    height: 18px;
    border-radius: 50%;
    background: var(--bullet-red);
  }
  .net-weight {
    position: absolute;
    left: 0;
    top: 531px;
    width: 365px;
    height: 92px;
    background: var(--brand-purple);
    color: var(--white);
    font-family: "Arimo", Arial, sans-serif;
    font-size: 38px;
    display: flex;
    align-items: center;
    justify-content: center;
  }
  .brand-mark {
    position: absolute;
    left: 612px;
    top: 200px;
    width: 262px;
    height: 262px;
    border-radius: 50%;
    background: var(--brand-purple);
  }
  .brand-name {
    position: absolute;
    left: 410px;
    top: 490px;
    width: 528px;
    margin: 0;
    text-align: center;
    font-family: "Arimo", Arial, sans-serif;
    font-weight: 700;
    font-size: 96px;
    line-height: 1;
    letter-spacing: 14px;
    color: var(--brand-purple);
  }
</style>
</head>
<body>
  <main class="canvas">
    <section class="label" aria-label="Styling gel jar label">
      <h1 class="product-title">STYLING GEL</h1>
      <ul class="claims">
        <li>Used by Professionals</li>
        <li>Maximum Hold</li>
        <li>Alcohol Free</li>
        <li>NO FLAKING</li>
      </ul>
      <div class="net-weight">16 oz.</div>
      <div class="brand-mark" aria-hidden="true"></div>
      <p class="brand-name">7 VEX</p>
    </section>
  </main>
</body>
</html>
```